TovaLamarpe - Israeli Mental Health Website

We are developing an Israeli website for mental health. The website will be both in English and in Hebrew. We have a logo and would like a website design based on the logo and the logos colors (attached).

Attached is a doc that contains the website requirements.

We would like to have an icon for each of the sidebar categories, an image for each of the pages (including each of the sidebar category pages).

Target Market(s)

Adults 18-80

Industry/Entity Type

Mental Health

Number of Pages Required

5+ page

Font styles to use
Sans Serif

Colors

Designer to choose colors to be used in the design.

```html
<!DOCTYPE html>
<html lang="en">
<head>
<meta charset="utf-8">
<title>TovaLamarpe - Israeli Mental Health</title>
<link rel="stylesheet" href="https://fonts.googleapis.com/css2?family=Raleway:wght@500;600;700&family=Lato:wght@400;700&display=swap">
<style>
:root{
  --blue:#2173bd;
  --green:#4ba843;
  --ink:#222;
  --text:#555;
  --page:#f8f8f8;
  --footer:#262626;
  --white:#fff;
}
*{box-sizing:border-box;margin:0;padding:0}
html,body{width:1200px;height:2417px;overflow:hidden}
body{position:relative;background:var(--page);font-family:'Lato',sans-serif;color:var(--text)}
.header{position:absolute;left:0;top:0;width:1200px;height:136px;background:var(--white)}
.brand{position:absolute;left:111px;top:44px;display:flex;align-items:center;gap:10px;font-family:'Raleway',sans-serif;font-weight:700;font-size:30px;color:var(--blue)}
.brand-dot{width:34px;height:34px;border-radius:50%;background:var(--green)}
.lang{position:absolute;left:906px;top:26px;font-family:'Raleway',sans-serif;font-size:18px;color:#444}
.lang::after{content:"";display:inline-block;margin-left:5px;border:5px solid transparent;border-top:6px solid #444;vertical-align:-1px}
.donate{position:absolute;left:973px;top:14px;width:115px;height:48px;border-radius:24px;background:var(--green);color:#fff;font-family:'Raleway',sans-serif;font-weight:600;font-size:18px;display:flex;align-items:center;justify-content:center}
.nav{position:absolute;right:112px;top:84px;display:flex;gap:25px;font-family:'Raleway',sans-serif;font-weight:500;font-size:17.5px;color:#222}
.sidebar{position:absolute;left:0;top:136px;width:369px;height:834px;background:var(--blue);padding-top:16px}
.cat{display:flex;align-items:center;height:61.7px;padding-left:43px;color:#fff;font-family:'Raleway',sans-serif;font-weight:600;font-size:18px}
.cat-icon{width:50px;height:50px;border-radius:50%;background:#fff;margin-right:16px;display:flex;align-items:center;justify-content:center;flex:none}
.cat-icon svg{width:30px;height:30px}
.intro{position:absolute;left:369px;top:136px;width:831px;height:239px;background:var(--page);padding:46px 0 0 31px}
.intro h1{font-family:'Raleway',sans-serif;font-weight:700;font-size:41px;color:var(--ink);letter-spacing:-.2px}
.intro p{margin-top:20px;width:700px;font-size:17.5px;line-height:26.5px;color:#555}
.hero{position:absolute;left:369px;top:375px;width:831px;height:595px;background:linear-gradient(100deg,#2a1c1a 0%,#3e2622 35%,#7d4a4a 60%,#b77989 80%,#5c6c8a 100%)}
.hero-copy{position:absolute;left:53px;top:74px;width:420px;color:#fff}
.hero-copy h2{font-family:'Raleway',sans-serif;font-weight:700;font-size:31px}
.hero-copy p{margin-top:22px;font-size:17px;line-height:25px}
.btn{display:flex;align-items:center;justify-content:center;border-radius:31px;background:var(--green);color:#fff;font-family:'Raleway',sans-serif;font-weight:700;font-size:19px}
.hero-copy .btn{margin-top:33px;margin-left:6px;width:202px;height:66px;font-size:17.5px}
.chat-fab{position:absolute;left:1135px;top:350px;width:66px;height:66px;border-radius:50%;background:var(--blue);display:flex;align-items:center;justify-content:center}
.services{position:absolute;left:111px;top:1035px;width:977px;display:grid;grid-template-columns:476px 476px;column-gap:25px;row-gap:58px}
.card-photo{height:302px;box-shadow:0 6px 14px rgba(0,0,0,.12)}
.card h3{margin-top:30px;font-family:'Raleway',sans-serif;font-weight:500;font-size:27px;color:var(--ink)}
.card p{margin-top:14px;font-size:17px;line-height:25px;color:#555}
.card .btn{margin-top:28px;width:200px;height:61px}
.footer{position:absolute;left:0;top:2312px;width:1200px;height:105px;background:var(--footer);color:#fff;font-size:17.5px}
.footer .copy{position:absolute;left:111px;top:42px}
.footer .legal{position:absolute;right:112px;top:42px}
</style>
</head>
<body>
<header class="header">
  <div class="brand"><span class="brand-dot"></span>TovaLamarpe</div>
  <div class="lang">Eng</div>
  <div class="donate">DONATE</div>
  <nav class="nav"><span>Smart ChatLine</span><span>Therapists</span><span>Organizations</span><span>Videos</span><span>Contact</span><span>About</span></nav>
</header>

<aside class="sidebar">
  <div class="cat"><span class="cat-icon"><svg viewBox="0 0 30 30"><circle cx="14" cy="12" r="9" fill="#4ba843"/><rect x="11" y="18" width="7" height="9" fill="#4ba843"/><path d="M12 12h6M15 9v6" stroke="#fff" stroke-width="2.2"/></svg></span>Emergency Mental Help</div>
  <div class="cat"><span class="cat-icon"><svg viewBox="0 0 30 30"><path d="M5 5l20 20M25 5L5 25" stroke="#4ba843" stroke-width="4" stroke-linecap="round"/></svg></span>Suicide</div>
  <div class="cat"><span class="cat-icon"><svg viewBox="0 0 30 30"><path d="M6 4l4 12h10l4-12" stroke="#4ba843" stroke-width="3" fill="none"/><rect x="9" y="18" width="12" height="9" fill="#4ba843"/></svg></span>Violence Victims</div>
  <div class="cat"><span class="cat-icon"><svg viewBox="0 0 30 30"><rect x="7" y="6" width="16" height="19" rx="6" fill="#4ba843"/></svg></span>Violence Assaulters</div>
  <div class="cat"><span class="cat-icon"><svg viewBox="0 0 30 30"><circle cx="14" cy="12" r="9" fill="#4ba843"/><rect x="10" y="18" width="8" height="9" fill="#4ba843"/></svg></span>Post Trauma</div>
  <div class="cat"><span class="cat-icon"><svg viewBox="0 0 30 30"><circle cx="15" cy="11" r="5" fill="#4ba843"/><path d="M5 27c0-7 4-10 10-10s10 3 10 10z" fill="#4ba843"/></svg></span>Depression</div>
  <div class="cat"><span class="cat-icon"><svg viewBox="0 0 30 30"><circle cx="15" cy="14" r="10" stroke="#4ba843" stroke-width="2.5" fill="none"/><path d="M15 8v8" stroke="#4ba843" stroke-width="3"/><circle cx="15" cy="20" r="1.8" fill="#4ba843"/></svg></span>Anxiety</div>
  <div class="cat"><span class="cat-icon"><svg viewBox="0 0 30 30"><path d="M6 24L22 8" stroke="#4ba843" stroke-width="5" stroke-linecap="round"/><path d="M20 4l6 6" stroke="#4ba843" stroke-width="2.5"/></svg></span>Addictions</div>
  <div class="cat"><span class="cat-icon"><svg viewBox="0 0 30 30"><path d="M4 14h8l-8 10h8M15 8h6l-6 7h6" stroke="#4ba843" stroke-width="2.5" fill="none"/></svg></span>Sleep Disorders</div>
  <div class="cat"><span class="cat-icon"><svg viewBox="0 0 30 30"><path d="M3 14h24a12 10 0 0 1-24 0z" fill="#4ba843"/><circle cx="15" cy="10" r="4" fill="#4ba843"/></svg></span>Eating Disorders</div>
  <div class="cat"><span class="cat-icon"><svg viewBox="0 0 30 30"><rect x="4" y="11" width="22" height="12" stroke="#4ba843" stroke-width="2.5" fill="none"/><circle cx="15" cy="17" r="3" fill="#4ba843"/></svg></span>Financial Problems</div>
  <div class="cat"><span class="cat-icon"><svg viewBox="0 0 30 30"><circle cx="15" cy="7" r="3.5" fill="#4ba843"/><rect x="12" y="11" width="6" height="9" fill="#4ba843"/><path d="M4 14c2 9 8 12 11 12s9-3 11-12" stroke="#4ba843" stroke-width="3" fill="none"/></svg></span>Parenthood</div>
  <div class="cat"><span class="cat-icon"><svg viewBox="0 0 30 30"><path d="M13 17l-5 5a4 4 0 0 1-5-5l5-5M17 13l5-5a4 4 0 0 1 5 5l-5 5M11 19l8-8" stroke="#4ba843" stroke-width="3" fill="none" stroke-linecap="round"/></svg></span>Relationship</div>
</aside>

<section class="intro">
  <h1>TovaLamarpe - Israeli Mental Health</h1>
  <p>Lorem ipsum dolor sit amet, consectetur adipiscing elit, sed do eiusmod tempor incididunt ut labore et dolore magna aliqua. Quis ipsum suspendisse ultrices gravida. Risus commodo viverra maecenas accumsan lacus vel facilisis.</p>
</section>

<section class="hero" role="img" aria-label="Photo of a therapist holding the hands of a client during a session">
  <div class="hero-copy">
    <h2>Emergency Mental Help</h2>
    <p>Lorem ipsum dolor sit amet, consectetur adipiscing elit, sed do eiusmod tempor incididunt ut labore et dolore magna aliqua. Ut enim ad minim veniam, quis nostrud exercitation ullamco laboris nisi ut aliquip ex ea commodo consequat.</p>
    <div class="btn">MORE OPTIONS</div>
  </div>
</section>

<div class="chat-fab"><svg width="32" height="32" viewBox="0 0 24 24"><path d="M6.6 10.8a15 15 0 0 0 6.6 6.6l2.2-2.2a1 1 0 0 1 1-.25 11 11 0 0 0 3.6.6 1 1 0 0 1 1 1V20a1 1 0 0 1-1 1A17 17 0 0 1 3 4a1 1 0 0 1 1-1h3.5a1 1 0 0 1 1 1 11 11 0 0 0 .6 3.6 1 1 0 0 1-.25 1z" fill="#fff"/></svg></div>

<main class="services">
  <article class="card">
    <div class="card-photo" role="img" aria-label="Photo of hands holding a smartphone with chat bubbles" style="background:linear-gradient(135deg,#1c3442,#3c5968 55,#a38576)"></div>
    <h3>Smart ChatLine</h3>
    <p>Lorem ipsum dolor sit amet, consectetur adipiscing elit, sed do eiusmod tempor incididunt ut labore et dolore magna aliqua. Ut enim ad minim veniam, quis nostrud exercitation ullamco laboris nisi ut aliquip ex.</p>
    <div class="btn">05X-XXXXXXX</div>
  </article>
  <article class="card">
    <div class="card-photo" role="img" aria-label="Photo of a therapist taking notes during a session with a client" style="background:linear-gradient(135deg,#5a6f8f,#c9b9c6 50%,#38425a)"></div>
    <h3>Therapists</h3>
    <p>Lorem ipsum dolor sit amet, consectetur adipiscing elit, sed do eiusmod tempor incididunt ut labore et dolore magna aliqua. Ut enim ad minim veniam, quis nostrud exercitation ullamco laboris nisi ut aliquip ex.</p>
    <div class="btn">Find Therapists</div>
  </article>
  <article class="card">
    <div class="card-photo" role="img" aria-label="Photo of a group stacking hands together in unity" style="background:linear-gradient(135deg,#e8e4df,#b78b6f 50%,#eef0f0)"></div>
    <h3>Organizations</h3>
    <p>Lorem ipsum dolor sit amet, consectetur adipiscing elit, sed do eiusmod tempor incididunt ut labore et dolore magna aliqua. Ut enim ad minim veniam, quis nostrud exercitation ullamco laboris nisi ut aliquip ex.</p>
    <div class="btn">Find Organizations</div>
  </article>
  <article class="card">
    <div class="card-photo" role="img" aria-label="Photo of clasped hands resting on a lap" style="background:linear-gradient(180deg,#e5cccf,#d8b8b8 60%,#34495a)"></div>
    <h3>Videos</h3>
    <p>Lorem ipsum dolor sit amet, consectetur adipiscing elit, sed do eiusmod tempor incididunt ut labore et dolore magna aliqua. Ut enim ad minim veniam, quis nostrud exercitation ullamco laboris nisi ut aliquip ex.</p>
    <div class="btn">Video Library</div>
  </article>
</main>

<footer class="footer">
  <div class="copy">TovaLamarpe - Organization for Mental Health ©2023</div>
  <div class="legal">Privacy Policy &nbsp;|&nbsp; Terms</div>
</footer>
</body>
</html>
```